DPW Business Card

This is a wide-range political consulting firm specializing in high-profile political campaigns. Red should be a predominant color in the business card, since this is a Lantern Party inspired consulting firm, but the word "lantern" will not appear anywhere in any kind of literature. Look has to be clean and crisp. The design should be forward thinking and appropriate for a company that is trying to break away from a traditionally "stodgy" image in politics.

Target Market(s)

potential national political candidates, wealthy donors,

Industry/Entity Type

Political

Contact Information for Business Card

Doran P. Whitcliffe
Political Consultant
437 Orchard Lane SE
#358
Washington, DC 20417

```html
<!DOCTYPE html>
<html lang="en">
<head>
<meta charset="UTF-8">
<title>DPW Business Card</title>
<link rel="stylesheet" href="https://fonts.googleapis.com/css2?family=Poppins:wght@400;600&display=swap">
<style>
  :root {
    --backdrop: #3b3b3d;
    --paper: #ececec;
    --red: #9c1c24;
    --red-light: #b3353c;
    --ink: #2b2b2b;
    --paper-text: #f4f4f4;
  }
  * { box-sizing: border-box; margin: 0; padding: 0; }
  html, body {
    width: 1200px;
    height: 900px;
    overflow: hidden;
    background: var(--backdrop);
    font-family: "Poppins", "Century Gothic", sans-serif;
  }
  .canvas {
    width: 1200px;
    height: 900px;
    display: flex;
    flex-direction: column;
    align-items: center;
    justify-content: center;
    gap: 60px;
  }
  .card {
    position: relative;
    width: 560px;
    height: 320px;
    padding: 58px 54px 0;
    overflow: hidden;
  }
  .card--front { background: var(--paper); color: var(--ink); }
  .card--back { background: var(--red); color: var(--paper-text); }

  .card__name {
    font-size: 24px;
    font-weight: 600;
    letter-spacing: 0.02em;
    text-transform: uppercase;
    line-height: 1.1;
  }
  .card__title {
    font-size: 14px;
    font-weight: 400;
    margin-top: 2px;
  }
  .card--front .card__title { color: var(--red); }

  .card__contact {
    position: absolute;
    left: 54px;
    bottom: 50px;
    font-size: 13px;
    line-height: 1.45;
  }
  .card__contact strong { font-weight: 600; }

  .card__band {
    position: absolute;
    left: 0;
    right: 0;
    bottom: 0;
    height: 24px;
  }
  .card--front .card__band {
    background: var(--red);
    border-top: 6px solid var(--red-light);
  }
  .card--back .card__band {
    background: var(--red-light);
    opacity: 0.75;
  }
</style>
</head>
<body>
<main class="canvas">
  <section class="card card--front">
    <h1 class="card__name">Doran P. Whitcliffe</h1>
    <p class="card__title">Political Consultant</p>
    <address class="card__contact" style="font-style:normal">
      <strong>Tel:</strong> 617-555-0142 · <strong>Email:</strong> DPWhitcliffe@inkpost.com<br>
      437 Orchard Lane SE #358, Washington, DC 20417
    </address>
    <div class="card__band"></div>
  </section>

  <section class="card card--back">
    <h2 class="card__name">Doran P. Whitcliffe</h2>
    <p class="card__title">Political Consultant</p>
    <address class="card__contact" style="font-style:normal">
      <strong>Tel:</strong> 617-555-0142 · <strong>Email:</strong> DPWhitcliffe@inkpost.com<br>
      437 Orchard Lane SE #358, Washington, DC 20417
    </address>
    <div class="card__band"></div>
  </section>
</main>
</body>
</html>
```